Banner Ad for Resume Writers

This ad is for www.kelbrancareers.com.au

The site offers a resume writing service in Australia. Take a look at the site for more info.

Colours to use: Blue, orange, yellow or whatever works.

Image specifications:
Pixel size: 160w X 600h (Skyscraper)
Image format: GIF (25K max)
Must have a border and must not use transparent backgrounds

Text can include:

'Professional Resume Writers'

and

'Is your resume good enough? Ask the Experts!'

The text 'Free resume health check' could be included but the banner should look good even if this text is not included as it may need to be removed.

Target Market(s)

Job seekers

Industry/Entity Type

Health

Nice to have
• It would be good to include an attractive smiling face making eye contact with the viewer.
Should not have
• Should not be too busy. Avoid clutter.

```html
<!DOCTYPE html>
<html lang="en">
<head>
<meta charset="utf-8">
<title>Static Banner – Kelbran Careers Skyscrapers</title>
<link rel="stylesheet" href="https://fonts.googleapis.com/css2?family=Oswald:wght@500;600;700&family=Arimo:wght@400;700&display=swap">
<style>
  :root {
    --stage-top: #4b4b4b;
    --stage-mid: #1c1c1c;
    --stage-bottom: #3c3c3c;
    --frame: #b9b9b9;
    --header-red: #e3151b;
    --header-red-dark: #a8070b;
    --divider-grey: #c9c9c9;
    --sky-light: #7fcbf0;
    --sky-mid: #2f98d2;
    --sky-deep: #1b6aa6;
    --gold-light: #fff7a0;
    --gold: #ffd61a;
    --gold-deep: #e0a400;
    --button-yellow: #fbf31a;
    --button-edge: #d8d8d8;
    --ink: #111111;
    --white: #ffffff;
  }
  * { box-sizing: border-box; margin: 0; padding: 0; }
  html, body { width: 1180px; height: 1200px; overflow: hidden; }
  body {
    background: linear-gradient(180deg, var(--stage-top) 0%, var(--stage-mid) 45%, var(--stage-bottom) 100%);
    font-family: "Oswald", "Arial Narrow", sans-serif;
    position: relative;
  }
  .board-title {
    position: absolute; left: 0; width: 1116px; top: 80px;
    text-align: center; color: var(--white);
    font-weight: 600; font-size: 66px; line-height: 1; letter-spacing: 0.5px;
  }
  .skyscraper {
    position: absolute; top: 200px; width: 250px; height: 937px;
    border: 3px solid var(--frame);
    background: linear-gradient(180deg, var(--sky-light) 0%, var(--sky-mid) 45%, var(--sky-deep) 100%);
    overflow: hidden;
  }
  .skyscraper--one { left: 163px; }
  .skyscraper--two { left: 434px; }
  .skyscraper--mining { left: 709px;
    background: linear-gradient(180deg, #5fc0ef 0%, #2c8fcb 40%, #1b6aa6 70%, #2b86c4 100%); }
  .brand-header {
    position: absolute; left: 0; top: 0; width: 100%; height: 180px;
    background: radial-gradient(ellipse at 50% 30%, var(--header-red) 0%, var(--header-red-dark) 100%);
    border-bottom: 10px solid var(--divider-grey);
    display: flex; align-items: center; justify-content: center;
    text-align: center; color: var(--white);
  }
  .brand-name {
    font-weight: 600; font-size: 46px; line-height: 54px;
  }
  .line {
    position: absolute; left: 0; width: 100%; text-align: center; white-space: nowrap;
  }
  .headline {
    font-weight: 700; text-transform: uppercase;
    background: linear-gradient(180deg, var(--gold-light) 0%, var(--gold) 50%, var(--gold-deep) 100%);
    -webkit-background-clip: text; background-clip: text; color: transparent;
    filter: drop-shadow(0 2px 1px rgba(0,40,90,0.6));
  }
  .headline--sm { top: 208px; font-size: 36px; line-height: 44px; }
  .headline--lg { top: 254px; font-size: 68px; line-height: 76px; }
  .headline--md { top: 330px; font-size: 60px; line-height: 66px; }
  .question {
    color: var(--white); font-weight: 500; font-size: 40px; line-height: 48px;
    text-shadow: 0 2px 2px rgba(0,30,70,0.6); letter-spacing: -0.5px;
  }
  .question--a { top: 420px; }
  .question--b { top: 468px; }
  .portrait {
    position: absolute; left: 0; top: 527px; width: 100%; height: 300px;
    background: radial-gradient(ellipse at 50% 55%, #f3d2b6 0%, #d9b28c 28%, #c9e6f6 62%, #9fd3f0 100%);
  }
  .cta {
    position: absolute; left: 9px; width: 226px; height: 90px;
    background: var(--button-yellow);
    border: 3px solid var(--button-edge);
    box-shadow: 0 2px 3px rgba(0,0,0,0.35);
    color: var(--ink); text-align: center;
    font-family: "Arimo", Arial, sans-serif; font-size: 25px; line-height: 34px;
    padding-top: 8px;
  }
  .skyscraper--one .cta, .skyscraper--two .cta { top: 828px; }
  .skyscraper--mining .cta { top: 820px; left: 11px; padding-top: 6px; }
  .mining-head--a { top: 220px; font-size: 74px; line-height: 84px; text-transform: none; }
  .mining-head--b { top: 304px; font-size: 58px; line-height: 66px; }
  .mining-head--c { top: 372px; font-size: 58px; line-height: 66px; }
  .mining-q--a { top: 512px; font-size: 42px; line-height: 50px; }
  .mining-q--b { top: 566px; font-size: 78px; line-height: 84px; letter-spacing: -1px; }
  .mining-q--c { top: 650px; font-size: 78px; line-height: 84px; letter-spacing: -1px; }
  .mining-q--d { top: 738px; font-size: 40px; line-height: 48px; }
</style>
</head>
<body>
  <h1 class="board-title">Static Banner</h1>

  <section class="skyscraper skyscraper--one">
    <header class="brand-header">
      <span class="brand-name">Kelbran<br>Careers</span>
    </header>
    <p class="line headline headline--sm">Professional</p>
    <p class="line headline headline--lg">Resume</p>
    <p class="line headline headline--md">Writers</p>
    <p class="line question question--a">Is your resume</p>
    <p class="line question question--b">good enough?</p>
    <div class="portrait" role="img" aria-label="Photo of a smiling young woman looking at the viewer"></div>
    <div class="cta">Ask the Experts<br>Click Here!</div>
  </section>

  <section class="skyscraper skyscraper--two">
    <header class="brand-header">
      <span class="brand-name">Kelbran<br>Careers</span>
    </header>
    <p class="line headline headline--sm">Professional</p>
    <p class="line headline headline--lg">Resume</p>
    <p class="line headline headline--md">Writers</p>
    <p class="line question question--a">Is your resume</p>
    <p class="line question question--b">good enough?</p>
    <div class="portrait" role="img" aria-label="Photo of a smiling young woman looking at the viewer"></div>
    <div class="cta">Ask the Experts<br>Click Here!</div>
  </section>

  <section class="skyscraper skyscraper--mining">
    <header class="brand-header">
      <span class="brand-name">Kelbran<br>Careers</span>
    </header>
    <p class="line headline mining-head--a">Mining</p>
    <p class="line headline mining-head--b">Resume</p>
    <p class="line headline mining-head--c">Writers</p>
    <p class="line question mining-q--a">Is your</p>
    <p class="line question mining-q--b">mining</p>
    <p class="line question mining-q--c">resume</p>
    <p class="line question mining-q--d">good enough?</p>
    <div class="cta">Get Started Now<br>Click Here!</div>
  </section>
</body>
</html>
```